Home Inspection Flyer

Looking to have flyer designed that features our business, services, and our contact information. There are three of us. We are all business partners and do not have a company phone number. So each of us would need to be listed on flyer along with our individual phone number. Everything you could possibly need is on our website from logo to services and contact information. https://larkmeadowhomereview.com/. If you could possible incorporate our company colors that would be great. You can find those in our logo top left hand side of website and attached. Please also include our velcorant and brev logos ( home inspector affiliations ) on brochure as well. Those can be found on website. Please feel free to reach out with any questions.
Thanks
Dale
Updates
Looking to get a few tri fold designs. All the ones submitted have been 8x11

```html
<!DOCTYPE html>
<html lang="en">
<head>
<meta charset="utf-8">
<title>Larkmeadow Home Review – Home Buyer Inspection Flyer</title>
<link href="https://fonts.googleapis.com/css2?family=Poppins:wght@400;500;600;700;800&display=swap" rel="stylesheet">
<style>
  :root{
    --green:#84f01a;
    --purple:#8a22d8;
    --black:#0b0b0b;
    --white:#ffffff;
    --ink:#141414;
    --photo-a:#d9d6d2;
    --photo-b:#8f8a86;
  }
  *{margin:0;padding:0;box-sizing:border-box}
  html,body{width:783px;height:1200px;overflow:hidden;background:var(--white)}
  body{font-family:"Poppins",sans-serif;color:var(--ink)}
  .flyer{position:relative;width:783px;height:1200px;overflow:hidden;background:var(--white)}

  .hero-art{position:absolute;left:0;top:0;width:783px;height:455px}

  .brand{position:absolute;left:61px;top:62px;display:flex;align-items:center;gap:10px}
  .brand-mark{width:22px;height:22px;background:var(--green)}
  .brand-name{font-weight:700;font-size:18px;letter-spacing:.5px;color:var(--black);line-height:1.1;width:150px}

  .headline{position:absolute;left:57px;top:208px;color:var(--white)}
  .headline h1{font-size:40px;line-height:42px;font-weight:400;letter-spacing:.3px}
  .headline .hl-green{color:var(--green);font-weight:800;display:block}
  .headline .hl-thin{display:block}
  .headline .hl-bold{font-weight:800;display:block}
  .headline .rule{width:44px;height:5px;border-radius:3px;background:var(--green);margin:14px 0 12px}
  .headline p{font-weight:700;font-size:13.5px;line-height:18px}

  .intro{position:absolute;left:0;top:458px;width:783px;height:92px;background:var(--purple);color:var(--white);padding:16px 60px 0}
  .intro h2{font-size:14.5px;font-weight:700;letter-spacing:.1px}
  .intro p{font-size:11.5px;line-height:15px;margin-top:6px}

  .services{position:absolute;left:61px;top:568px;width:220px}
  .services h3{font-size:14.5px;font-weight:700;line-height:19px;color:var(--black)}
  .services h3 span{color:var(--purple);display:block}
  .services .hint{font-size:11.5px;line-height:14px;margin:6px 0 6px}

  .ticks{list-style:none}
  .ticks li{position:relative;padding-left:21px;font-size:11.5px;font-weight:500;line-height:14px}
  .ticks li::before{content:"";position:absolute;left:2px;top:3px;width:8px;height:8px;border-radius:50%;background:var(--purple);box-shadow:inset 0 0 0 2px var(--purple)}
  .ticks li::after{content:"";position:absolute;left:4.5px;top:5px;width:3px;height:2px;border-left:1.2px solid #fff;border-bottom:1.2px solid #fff;transform:rotate(-45deg)}
  .services .ticks li{margin-bottom:7px}

  .photo{position:absolute;width:136px;height:102px;border:3px solid #fff;border-radius:4px;box-shadow:0 2px 6px rgba(0,0,0,.25)}
  .photo.p1{left:302px;top:571px;background:linear-gradient(160deg,#f2eee9,#b9b2aa)}
  .photo.p2{left:464px;top:571px;background:linear-gradient(180deg,#8fb4dd 0%,#cfd7df 45%,#6e8f4d 100%)}
  .photo.p3{left:302px;top:689px;background:linear-gradient(135deg,#cfcfcf,#7a6f63 60%,#e0b36a)}
  .photo.p4{left:464px;top:689px;background:linear-gradient(160deg,#d8c6a4,#4a5a45 60%,#9f8e7a)}

  .badge{position:absolute;width:100px;height:100px;border-radius:50%}
  .badge.b1{left:622px;top:575px;background:radial-gradient(circle,#8d8a82 0 55%,#3a3a3a 56% 100%)}
  .badge.b2{left:622px;top:693px;background:radial-gradient(circle,#f2cf3a 0 55%,#c99a12 56% 100%)}

  .benefits-title{position:absolute;left:0;top:820px;width:783px;text-align:center;font-size:14.5px;font-weight:700;color:var(--black)}
  .benefits-title span{color:var(--purple)}
  .divider{position:absolute;left:191px;top:851px;width:400px;height:1px;background:#cfcfcf}
  .divider::after{content:"";position:absolute;left:175px;top:-2px;width:50px;height:5px;border-radius:3px;background:var(--green)}

  .benefits{position:absolute;top:878px}
  .benefits.left{left:61px;width:260px}
  .benefits.right{left:418px;width:280px}
  .benefits li{margin-bottom:10px}

  .contact-tab{position:absolute;left:0;top:1045px;width:783px;height:38px}
  .contact-tab .label{position:absolute;left:63px;top:7px;font-size:17px;font-weight:700;color:var(--black)}
  .contact-tab .label span{font-weight:400}

  .footer{position:absolute;left:0;top:1083px;width:783px;height:117px;background:var(--black);display:flex;padding:22px 0 0 82px}
  .person{color:#fff;font-size:11px;line-height:17px;padding-right:20px}
  .person + .person{border-left:1px dashed #6a6a6a;padding-left:20px}
  .person.c1{width:234px}
  .person.c2{width:227px}
  .person h4{color:var(--purple);font-size:16px;font-weight:700;line-height:20px}
  .person .row{display:flex;align-items:center;gap:6px}
  .person svg{width:10px;height:10px;flex:none}
</style>
</head>
<body>
<main class="flyer">

  <svg class="hero-art" viewBox="0 0 783 455" aria-hidden="false">
    <defs>
      <linearGradient id="photoTone" x1="0" y1="0" x2="1" y2="1">
        <stop offset="0" stop-color="var(--photo-a)"/>
        <stop offset="1" stop-color="var(--photo-b)"/>
      </linearGradient>
      <linearGradient id="fadeDark" x1="0" y1="0" x2="1" y2="0">
        <stop offset="0" stop-color="#0b0b0b" stop-opacity="1"/>
        <stop offset="1" stop-color="#0b0b0b" stop-opacity="0"/>
      </linearGradient>
    </defs>
    <rect x="0" y="0" width="783" height="455" fill="#ffffff"/>
    <rect x="0" y="170" width="783" height="285" fill="#0b0b0b"/>
    <polygon points="602,0 783,0 783,138" fill="var(--green)"/>
    <polygon points="300,170 493,40 520,40 327,170" fill="#0b0b0b"/>
    <polygon points="245,170 470,12 500,12 275,170" fill="#0b0b0b" opacity="0"/>
    <polygon points="236,162 480,8 540,8 296,162" fill="#0b0b0b"/>
    <g role="img" aria-label="Photo: smiling young family sitting on the floor of their new home under a cardboard roof">
      <polygon points="330,172 560,22 783,152 783,455 330,455" fill="url(#photoTone)"/>
    </g>
    <rect x="280" y="170" width="260" height="285" fill="url(#fadeDark)"/>
    <polyline points="322,174 560,20 783,150" fill="none" stroke="#ffffff" stroke-width="6"/>
    <rect x="0" y="162" width="330" height="6" fill="#ffffff" opacity="0"/>
  </svg>

  <div class="brand">
    <span class="brand-mark"></span>
    <span class="brand-name">LARKMEADOW HOME REVIEW</span>
  </div>

  <section class="headline">
    <h1><span class="hl-green">HOME BUYER</span><span class="hl-thin">INSPECTION</span><span class="hl-bold">RESIDENTIAL</span></h1>
    <div class="rule"></div>
    <p>A Home Buyer Inspection Is The Smart<br>Move But Don't Take Our Word For It</p>
  </section>

  <section class="intro">
    <h2>WHAT IS A LARKMEADOW HOME BUYER INSPECTION?</h2>
    <p>A home buyer inspection is a visual examination of a home and its systems: interior plumbing, electrical, roof, attics (temperature permitting), and visible areas of walls, ceilings, floors, foundations, etc. No house is perfect.</p>
  </section>

  <section class="services">
    <h3>LARKMEADOW HOME REVIEW <span>INSPECTION SERVICES</span></h3>
    <p class="hint">Select An Inspection Or Testing Service For More Information</p>
    <ul class="ticks">
      <li>Home Inspection</li>
      <li>Pest Inspection</li>
      <li>Radon Inspection</li>
      <li>Sewer Camera Inspection</li>
      <li>Water Sample Test</li>
      <li>Well Flow Test</li>
      <li>Septic Dye Flow Test</li>
    </ul>
  </section>

  <div class="photo p1" role="img" aria-label="Photo: mother lifting a child in a bright living room"></div>
  <div class="photo p2" role="img" aria-label="Photo: large two-storey suburban house with lawn"></div>
  <div class="photo p3" role="img" aria-label="Photo: hand holding a miniature model of a lit room"></div>
  <div class="photo p4" role="img" aria-label="Photo: inspectors reviewing house plans at a table"></div>
  <div class="badge b1" role="img" aria-label="Velcorant certified inspector badge"></div>
  <div class="badge b2" role="img" aria-label="Brev society of home inspectors badge"></div>

  <h3 class="benefits-title">LARKMEADOW HOME REVIEW'S <span>BENEFITS &amp; CREDENTIALS</span></h3>
  <div class="divider"></div>

  <ul class="ticks benefits left">
    <li>Fast, Reliable, Affordable Pricing</li>
    <li>Available On Evenings And Weekends</li>
    <li>Agent - Realtor Access Keys</li>
    <li>48 Hour Reporting</li>
    <li>Licensed By State Of Pennsylvania</li>
    <li>Members Of Brev Society Of<br>Home Inspectors</li>
  </ul>
  <ul class="ticks benefits right">
    <li>Members Of Velcorant Certified<br>Home Inspectors</li>
    <li>Abide By The Brev Code Of Ethics</li>
    <li>Continuous Learning And Professional<br>Development</li>
    <li>Professional Level Of Liability Insurance</li>
    <li>Nationally Accredited B.S. Business &amp;<br>Marketing Degrees</li>
    <li>Additional Services Available</li>
  </ul>

  <div class="contact-tab">
    <svg width="783" height="38" viewBox="0 0 783 38" aria-hidden="true">
      <polygon points="0,0 188,0 198,34 0,34" fill="var(--green)"/>
      <rect x="0" y="34" width="783" height="4" fill="var(--green)"/>
    </svg>
    <div class="label">CONTACT <span>US</span></div>
  </div>

  <footer class="footer">
    <div class="person c1">
      <h4>CORWIN HALE</h4>
      <div class="row"><svg viewBox="0 0 10 10"><path d="M2 1l2 2-1 1.2c.6 1.3 1.5 2.2 2.8 2.8L7 6l2 2-1.3 1.3C4.5 9 1 5.5.7 2.3z" fill="var(--green)"/></svg>(724) 555-0142</div>
      <div class="row"><svg viewBox="0 0 10 10"><rect x=".5" y="2" width="9" height="6" fill="var(--green)"/><path d="M.5 2L5 5.5 9.5 2" fill="none" stroke="#0b0b0b" stroke-width=".8"/></svg>corwin@larkmeadowhomereview.com</div>
    </div>
    <div class="person c2">
      <h4>REESE ALDANA</h4>
      <div class="row"><svg viewBox="0 0 10 10"><path d="M2 1l2 2-1 1.2c.6 1.3 1.5 2.2 2.8 2.8L7 6l2 2-1.3 1.3C4.5 9 1 5.5.7 2.3z" fill="var(--green)"/></svg>(412) 555-0187</div>
      <div class="row"><svg viewBox="0 0 10 10"><rect x=".5" y="2" width="9" height="6" fill="var(--green)"/><path d="M.5 2L5 5.5 9.5 2" fill="none" stroke="#0b0b0b" stroke-width=".8"/></svg>reese@larkmeadowhomereview.com</div>
    </div>
    <div class="person c3">
      <h4>DALE VARNICK</h4>
      <div class="row"><svg viewBox="0 0 10 10"><path d="M2 1l2 2-1 1.2c.6 1.3 1.5 2.2 2.8 2.8L7 6l2 2-1.3 1.3C4.5 9 1 5.5.7 2.3z" fill="var(--green)"/></svg>(412) 555-0129</div>
      <div class="row"><svg viewBox="0 0 10 10"><rect x=".5" y="2" width="9" height="6" fill="var(--green)"/><path d="M.5 2L5 5.5 9.5 2" fill="none" stroke="#0b0b0b" stroke-width=".8"/></svg>dale@larkmeadowhomereview.com</div>
    </div>
  </footer>

</main>
</body>
</html>
```